Wellspring Care Alliance Vonzo Ads

We want an ad created for the gay dating app vonzo. The size is 300x250. We want the ad to be sexy, with a shirtless man. We are advertising our free HIV and PrEP services. We are open to slogans about maybe "Bringing HIV and PrEP To You"
"Free PrEP and HIV Management"
Open to ideas.

We also offer through the Harborlight Support Fund
Copay Assistance, Insurance Premium Assistance, Free Medical Services, etc
Our website is wcanj.org

I do want the ad to have a Book Now Button

Gay sexually active males

```html
<!DOCTYPE html>
<html lang="en">
<head>
<meta charset="utf-8">
<title>Wellspring Care Alliance — Vonzo Ads</title>
<link href="https://fonts.googleapis.com/css2?family=Poppins:wght@600;700;800&display=swap" rel="stylesheet">
<style>
  :root{
    --stage:#b3b3b3;
    --white:#ffffff;
    --ink:#2b2b2b;
    --brand:#3b6fd6;
    --cta:#f2504a;
    --purple-deep:#2a0a78;
    --purple:#7a1fd6;
    --magenta:#d23be0;
    --band-start:#6a2cf5;
    --band-end:#ff4d5a;
    --sky-light:#eef2f6;
    --sky-mid:#cfdbe6;
    --skin-light:#e3b89a;
    --skin-dark:#b88466;
  }
  *{box-sizing:border-box;margin:0;padding:0}
  html,body{width:1200px;height:565px;overflow:hidden;background:var(--stage);font-family:"Poppins",Arial,sans-serif}
  .canvas{position:relative;width:1200px;height:565px}
  .ad{position:absolute;top:84px;width:474px;height:395px;overflow:hidden}
  .ad--bring{left:82px;background:radial-gradient(circle at 62% 45%,var(--magenta) 0%,var(--purple) 35%,var(--purple-deep) 75%)}
  .ad--free{left:643px;background:linear-gradient(120deg,var(--sky-light) 0%,var(--sky-mid) 55%,var(--sky-light) 100%)}
  .brand{position:absolute;left:32px;top:13px;width:186px;height:73px;display:flex;align-items:center;gap:8px;padding:0 10px}
  .ad--bring .brand{background:var(--white)}
  .brand__dot{flex:none;width:16px;height:16px;border-radius:50%;background:var(--brand)}
  .brand__name{font-weight:700;font-size:15px;line-height:1.1;color:var(--brand)}
  .headline{position:absolute;left:32px;font-weight:800;font-size:26px;line-height:1.15;text-transform:uppercase}
  .ad--bring .headline{top:118px;color:var(--white)}
  .ad--free .headline{top:96px;color:var(--ink)}
  .cta{position:absolute;left:32px;height:28px;background:var(--cta);color:var(--white);font-weight:700;font-size:12px;display:flex;align-items:center;justify-content:center;text-transform:uppercase}
  .ad--bring .cta{top:221px;width:114px}
  .ad--free .cta{top:308px;width:108px}
  .model{position:absolute;border-radius:90px 90px 0 0}
  .ad--bring .model{left:232px;top:24px;width:242px;height:371px;background:linear-gradient(180deg,var(--skin-light),var(--skin-dark))}
  .ad--free .model{left:250px;top:10px;width:210px;height:385px;border:6px solid var(--white);border-bottom:none;background:linear-gradient(180deg,var(--skin-light),var(--skin-dark))}
  .offer-band{position:absolute;left:19px;top:287px;width:439px;height:82px;background:linear-gradient(90deg,var(--band-start),var(--band-end));border-left:12px solid var(--white);border-right:12px solid var(--white);display:flex;align-items:center;justify-content:center;padding:0 22px}
  .offer-band p,.offer-copy{font-weight:700;font-size:12.5px;line-height:1.3}
  .offer-band p{color:var(--white);text-align:center}
  .offer-copy{position:absolute;left:32px;top:198px;width:200px;color:var(--ink)}
  .accent{position:absolute;left:0;top:0}
</style>
</head>
<body>
<div class="canvas">

  <section class="ad ad--bring">
    <div class="model" role="img" aria-label="Shirtless man standing, cut out against the background"></div>
    <div class="brand"><span class="brand__dot"></span><span class="brand__name">Wellspring Care Alliance</span></div>
    <h2 class="headline">Bringing HIV<br>and PrEP to<br>you</h2>
    <div class="cta">Book Now</div>
    <div class="offer-band"><p>We also offer through the Harborlight Support Fund Copay Assistance, Insurance Premium Assistance, Free Medical Services, etc</p></div>
  </section>

  <section class="ad ad--free">
    <svg class="accent" width="474" height="395" viewBox="0 0 474 395" aria-hidden="true">
      <polygon points="474,120 474,395 360,395" fill="#f2504a"/>
      <polygon points="200,395 330,300 474,395" fill="#8a2fe0"/>
    </svg>
    <div class="model" role="img" aria-label="Shirtless man with hands on hips, outlined in white"></div>
    <div class="brand"><span class="brand__dot"></span><span class="brand__name">Wellspring Care Alliance</span></div>
    <h2 class="headline">Free PrEP<br>and HIV<br>Management</h2>
    <p class="offer-copy">We also offer through the Harborlight Support Fund Copay Assistance, Insurance Premium Assistance, Free Medical Services, etc</p>
    <div class="cta">Book Now</div>
  </section>

</div>
</body>
</html>
```